Web Design for ROLV Air conditioning company

Hello,

I am calling on you for the modernization of the company's website
https://clarovent-services-techniques.fr/

The new one must include the new logo with the new graphic charter (color, style ...)

I'm looking for a simple design (less is more), a font written without Serif, the logo that brings a touch of color and modernity.

(maintenance and installation company for air conditioning and ventilation systems)
COLORS: in line with the logo

CHAPTER:

# PRESENTATION
# SERVICES
AIR CONDITIONING (ice cube icon)
HEATING (flame icon)
AIR TREATMENT (icon fan)
# ACHIEVEMENTS

# CONTACT
CONTACT FORM
GOOGLE MAPS

Target Market(s)

Showcase site for our customers

Coding

Coded - Design and coding required

Number of Pages Required

4 page

Font styles to use
Sans Serif

Colors
33b8a4
33a6d7
3176b5
ffffff

Requirements
Must have
• Clear and fluid navigation
a visual identity of the page with the logo
Should not have
• Overloaded.

```html
<!DOCTYPE html>
<html lang="en">
<head>
<meta charset="utf-8">
<title>ROLV – Climate Control Services</title>
<link href="https://fonts.googleapis.com/css2?family=Poppins:wght@400;500;600;700&display=swap" rel="stylesheet">
<style>
:root{
  --teal:#33b8a4;
  --blue:#33a6d7;
  --navy:#3176b5;
  --white:#ffffff;
  --ink:#2f3a42;
  --text:#4a4f55;
  --grey:#eeeded;
  --line:#d9d9d9;
}
*{box-sizing:border-box;margin:0;padding:0}
html,body{width:1200px;height:4000px;overflow:hidden;background:var(--white)}
body{position:relative;font-family:'Poppins',sans-serif;color:var(--text)}
.abs{position:absolute}
.brand{font-family:'Poppins',sans-serif;font-weight:700;color:var(--ink);letter-spacing:2px;display:flex;align-items:center;gap:12px}
.brand-mark{width:14px;height:14px;background:var(--teal)}

/* header */
.site-header{top:0;left:0;width:1200px;height:96px;background:var(--white);box-shadow:0 2px 6px rgba(0,0,0,.12);z-index:3}
.site-header .brand{left:67px;top:22px;font-size:44px;line-height:52px}
.main-nav{left:405px;top:38px;display:flex;gap:27px;font-size:14px;color:var(--ink)}
.main-nav a{color:inherit;text-decoration:none;position:relative}
.main-nav a.active{color:var(--blue)}
.main-nav a.active::after{content:"";position:absolute;left:-4px;right:-4px;bottom:-14px;height:3px;background:var(--blue)}
.hotline{left:918px;top:20px;display:flex;gap:12px;align-items:center}
.hotline small{display:block;color:var(--teal);font-size:14px;font-weight:500}
.hotline strong{display:block;color:var(--ink);font-size:21px;font-weight:600;line-height:26px}

/* hero */
.hero{top:96px;left:0;width:1200px;height:661px;background:linear-gradient(100deg,#dfe3e7 0%,#eef0f2 40%,#c7ced6 75%,#9aa8b6 100%)}
.hero-rule{top:757px;left:0;width:1200px;height:5px;background:linear-gradient(90deg,var(--teal),var(--navy))}
.hero-copy{left:130px;top:283px}
.hero-copy h1{font-size:33px;font-weight:700;color:var(--ink);line-height:40px}
.hero-copy p{margin-top:22px;font-size:21px;line-height:29px;color:var(--ink)}
.btn{display:inline-flex;align-items:center;justify-content:center;font-weight:600;font-size:15px;text-decoration:none}
.btn-fill{left:132px;top:461px;width:157px;height:43px;background:linear-gradient(90deg,var(--teal),var(--blue));color:var(--white)}
.btn-white{left:304px;top:461px;width:157px;height:43px;background:var(--white);color:var(--ink)}
.btn-outline{border:2px solid var(--teal);color:var(--teal);border-radius:24px;background:transparent}

/* about */
.about-title{left:130px;top:886px;font-size:42px;font-weight:700;color:var(--navy)}
.about-title span{color:var(--teal)}
.about-sub{left:130px;top:950px;font-size:18px;font-weight:600;color:var(--ink)}
.about-text{left:130px;top:992px;width:470px;font-size:17px;line-height:26px;color:var(--ink)}
.about-text p+p{margin-top:12px}
.about-btn{left:130px;top:1189px;width:168px;height:48px}

/* services */
.services{top:1327px;left:0;width:1200px;height:750px;background:var(--grey)}
.section-title{width:1200px;left:0;text-align:center;font-size:44px;font-weight:700;color:var(--ink)}
.section-title span{color:var(--teal)}

/* spirit */
.spirit{top:2077px;left:0;width:1200px;height:557px;background:linear-gradient(90deg,var(--teal) 0%,var(--blue) 35%,var(--navy) 60%);overflow:hidden}
.spirit h2{left:130px;top:96px;font-size:30px;font-weight:700;color:var(--white)}
.spirit .kicker{left:130px;top:150px;font-size:15px;color:var(--white);letter-spacing:.3px}
.check-list{left:130px;top:202px;list-style:none}
.check-list li{display:flex;align-items:center;gap:14px;height:38px;font-size:15px;font-weight:600;color:var(--white)}

/* climate */
.climate-title{top:2698px}
.climate-title span{margin-left:10px}
.step{font-size:13px;line-height:21px;color:var(--text)}
.step h3{font-size:20px;font-weight:700;color:var(--ink);margin-bottom:6px}
.step.right-al{text-align:right}

/* contact */
.contact{top:3244px;left:0;width:1200px;height:416px;background:var(--grey)}
.contact h2{top:76px;font-size:35px;color:var(--teal);background:linear-gradient(90deg,var(--teal),var(--blue));-webkit-background-clip:text;background-clip:text;color:transparent}
.field{background:var(--white);border:1px solid #e2e2e2;font-size:17px;color:var(--text);padding:10px 20px;font-family:inherit}
.send-btn{left:517px;top:312px;width:166px;height:46px}

/* footer */
.site-footer .brand{left:140px;top:3738px;font-size:62px}
.socials{left:158px;top:3834px;display:flex;gap:6px}
.socials span{width:31px;height:31px;border:2px solid var(--navy);border-radius:50%}
.foot-col h4{font-size:20px;font-weight:600;color:var(--ink);margin-bottom:10px}
.foot-col li{list-style:none;font-size:14px;line-height:27px;color:var(--navy)}
.contact-col li{display:flex;gap:10px;color:var(--ink);line-height:21px;margin-bottom:16px}
.copyright{top:3919px;left:0;width:1200px;border-top:1px solid var(--line);text-align:center;padding-top:26px;font-size:14px;color:var(--ink)}
</style>
</head>
<body>

<header class="site-header abs">
  <div class="brand abs"><span class="brand-mark"></span>ROLV</div>
  <nav class="main-nav abs">
    <a class="active" href="#">HOME</a><a href="#">ABOUT</a><a href="#">SERVICES ▾</a><a href="#">ACHIEVEMENTS</a><a href="#">CONTACT</a>
  </nav>
  <div class="hotline abs">
    <svg width="54" height="54" viewBox="0 0 54 54"><circle cx="27" cy="27" r="24" fill="none" stroke="#33a6d7" stroke-width="3"/><path d="M19 17c2-2 4 2 5 4s-2 3-1 5 4 5 6 6 3-2 5-1 5 3 3 5-5 3-9 0-11-9-12-12 1-5 3-7z" fill="#33a6d7"/></svg>
    <div><small>24/7 fasr service</small><strong>1 800 555 0142</strong></div>
  </div>
</header>

<section class="hero abs" role="img" aria-label="Photo of a technician on a step ladder servicing a wall-mounted air conditioner while a customer watches"></section>
<div class="hero-rule abs"></div>
<div class="hero-copy abs">
  <h1>CLAROVENT SERVICES<br>TECHNIQUES LYON</h1>
  <p>THE SOLUTION TO YOUR<br>MAINTENANCE PROBLEM</p>
</div>
<a class="btn btn-fill abs" href="#">READ MORE</a>
<a class="btn btn-white abs" href="#">GET A QUOTE</a>
<svg class="abs" style="left:41px;top:380px" width="52" height="52" viewBox="0 0 52 52"><circle cx="26" cy="26" r="23" fill="none" stroke="#5b6670" stroke-width="2"/><path d="M29 16l-10 10 10 10" fill="none" stroke="#5b6670" stroke-width="2.5"/></svg>
<svg class="abs" style="left:1107px;top:380px" width="50" height="50" viewBox="0 0 50 50"><circle cx="25" cy="25" r="24" fill="#33a6d7"/><path d="M21 15l10 10-10 10" fill="none" stroke="#fff" stroke-width="3"/></svg>

<!-- about -->
<h2 class="about-title abs">ABOUT <span>ROLV</span></h2>
<div class="about-sub abs">MAINTENANCE OF WATER TREATMENT SYSTEM</div>
<div class="about-text abs">
  <p>Lorem Ipsum is simply dummy text of the printing and typesetting industry. Lorem Ipsum has</p>
  <p>industry's standard dummy text ever since the 1500s, when an unknown printer took a galley of type and scrambled Lorem Ipsum is simply dummy text of the printing and typesetting industry.</p>
</div>
<a class="btn btn-outline about-btn abs" href="#">LEARN MORE</a>
<svg class="abs" style="left:659px;top:856px" width="408" height="408" viewBox="0 0 408 408">
  <defs><linearGradient id="aboutPhoto" x1="0" y1="0" x2="1" y2="1"><stop offset="0" stop-color="#e8e6e3"/><stop offset=".55" stop-color="#b9a596"/><stop offset="1" stop-color="#7d8a96"/></linearGradient></defs>
  <polygon points="120,3 288,3 405,120 405,288 288,405 120,405 3,288 3,120" fill="none" stroke="#33a6d7" stroke-width="5"/>
  <polygon role="img" aria-label="Photo of a technician in a hard hat working on a ceiling ventilation unit" points="124,16 284,16 392,124 392,284 284,392 124,392 16,284 16,124" fill="url(#aboutPhoto)"/>
</svg>

<!-- services -->
<section class="services abs">
  <h2 class="section-title abs" style="top:62px">OUR <span>SERVICES</span></h2>
</section>
<svg class="abs" style="left:0;top:1460px" width="1200" height="530" viewBox="0 1460 1200 530" font-family="Poppins, sans-serif" text-anchor="middle">
  <!-- left -->
  <polygon points="247,1468 407,1468 521,1582 521,1744 407,1858 247,1858 133,1744 133,1582" fill="none" stroke="#33a6d7" stroke-width="5"/>
  <polygon points="251,1480 403,1480 509,1586 509,1740 403,1846 251,1846 145,1740 145,1586" fill="#33a6d7"/>
  <!-- right -->
  <polygon points="789,1468 952,1468 1066,1582 1066,1744 952,1858 789,1858 675,1744 675,1582" fill="none" stroke="#3176b5" stroke-width="5"/>
  <polygon points="793,1480 948,1480 1054,1586 1054,1740 948,1846 793,1846 687,1740 687,1586" fill="#3176b5"/>
  <!-- centre -->
  <polygon points="516,1586 679,1586 793,1700 793,1862 679,1976 516,1976 402,1862 402,1700" fill="#fff" stroke="#33b8a4" stroke-width="5"/>
  <polygon points="521,1598 674,1598 781,1705 781,1857 674,1964 521,1964 414,1857 414,1705" fill="#33b8a4"/>

  <g fill="#fff">
    <!-- air conditioning: cubes -->
    <g fill="none" stroke="#fff" stroke-width="2.5" stroke-linejoin="round">
      <path d="M296 1534l18-9 18 9v20l-18 9-18-9z M296 1534l18 9 18-9 M314 1543v20"/>
      <path d="M332 1558l16-8 16 8v18l-16 8-16-8z M332 1558l16 8 16-8 M348 1566v18"/>
    </g>
    <text x="281" y="1645" font-size="20" font-weight="600">AIR CONDITIONING</text>
    <text x="294" y="1673" font-size="12.5">Lorem ipsum dolor sit amet</text>
    <text x="281" y="1692" font-size="12.5">consectetur adipisicing elit, sed</text>
    <text x="294" y="1711" font-size="12.5">do eiusmod tempor</text>
    <circle cx="328" cy="1763" r="16" fill="none" stroke="#fff" stroke-width="2"/>
    <path d="M320 1760l8 8 8-8" fill="none" stroke="#fff" stroke-width="2"/>

    <!-- heating: flame burst -->
    <polygon points="598,1660 604,1684 622,1672 612,1692 634,1696 612,1704 626,1722 604,1712 598,1738 592,1712 570,1722 584,1704 562,1696 584,1692 574,1672 592,1684" fill="none" stroke="#fff" stroke-width="2.5" stroke-linejoin="round"/>
    <text x="598" y="1796" font-size="20" font-weight="600">HEATING</text>
    <text x="598" y="1822" font-size="12.5">Lorem ipsum dolor sit amet</text>
    <text x="598" y="1841" font-size="12.5">consectetur adipisicing elit, sed</text>
    <text x="598" y="1860" font-size="12.5">do eiusmod tempor</text>
    <circle cx="598" cy="1905" r="16" fill="none" stroke="#fff" stroke-width="2"/>
    <path d="M590 1902l8 8 8-8" fill="none" stroke="#fff" stroke-width="2"/>

    <!-- air treatment: fan -->
    <g fill="none" stroke="#fff" stroke-width="2.5">
      <circle cx="854" cy="1565" r="6"/>
      <path d="M854 1559c-12-6-10-26 4-26s16 18 4 24z"/>
      <path d="M860 1565c6-12 26-10 26 4s-18 16-24 4z"/>
      <path d="M854 1571c12 6 10 26-4 26s-16-18-4-24z"/>
      <path d="M848 1565c-6 12-26 10-26-4s18-16 24-4z"/>
    </g>
    <text x="813" y="1645" font-size="20" font-weight="600" text-anchor="start">AIR TREATMENT</text>
    <text x="814" y="1673" font-size="12.5" text-anchor="start">Lorem ipsum dolor sit amet</text>
    <text x="814" y="1692" font-size="12.5" text-anchor="start">consectetur adipisicing elit, sed</text>
    <text x="814" y="1711" font-size="12.5" text-anchor="start">do eiusmod tempor</text>
    <circle cx="871" cy="1763" r="16" fill="none" stroke="#fff" stroke-width="2"/>
    <path d="M863 1760l8 8 8-8" fill="none" stroke="#fff" stroke-width="2"/>
  </g>
</svg>

<!-- spirit of service -->
<section class="spirit abs">
  <svg class="abs" style="left:0;top:0" width="1200" height="557" viewBox="0 0 1200 557">
    <defs><linearGradient id="gaugePhoto" x1="0" y1="0" x2="1" y2="1"><stop offset="0" stop-color="#dfe4e8"/><stop offset=".5" stop-color="#9aa4ae"/><stop offset="1" stop-color="#c9ced3"/></linearGradient></defs>
    <circle cx="1090" cy="283" r="478" fill="#fff"/>
    <circle role="img" aria-label="Photo of hands holding a refrigerant pressure gauge set beside an outdoor air conditioning unit" cx="1090" cy="283" r="470" fill="url(#gaugePhoto)"/>
    <line x1="0" y1="115" x2="96" y2="115" stroke="#fff" stroke-width="1.5" stroke-dasharray="3 3"/>
    <circle cx="101" cy="115" r="5" fill="#fff"/>
    <line x1="295" y1="460" x2="295" y2="527" stroke="#fff" stroke-width="1.5" stroke-dasharray="3 3"/>
    <circle cx="295" cy="530" r="5" fill="#fff"/>
  </svg>
  <h2 class="abs">ROLV – THE SPIRIT OF SERVICE</h2>
  <div class="kicker abs">MAINTENANCE OF WATER TREATMENT SYSTEM</div>
  <ul class="check-list abs">
    <li><svg width="24" height="24" viewBox="0 0 24 24"><path d="M20 12a8 8 0 1 1-4-7" fill="none" stroke="#fff" stroke-width="2"/><path d="M8 12l4 4 9-10" fill="none" stroke="#fff" stroke-width="2"/></svg>SOFT WATER</li>
    <li><svg width="24" height="24" viewBox="0 0 24 24"><path d="M20 12a8 8 0 1 1-4-7" fill="none" stroke="#fff" stroke-width="2"/><path d="M8 12l4 4 9-10" fill="none" stroke="#fff" stroke-width="2"/></svg>MAINTENANCE OF SOFTENERS</li>
    <li><svg width="24" height="24" viewBox="0 0 24 24"><path d="M20 12a8 8 0 1 1-4-7" fill="none" stroke="#fff" stroke-width="2"/><path d="M8 12l4 4 9-10" fill="none" stroke="#fff" stroke-width="2"/></svg>TREATMENT OF LIQUID EFFLUENTS</li>
    <li><svg width="24" height="24" viewBox="0 0 24 24"><path d="M20 12a8 8 0 1 1-4-7" fill="none" stroke="#fff" stroke-width="2"/><path d="M8 12l4 4 9-10" fill="none" stroke="#fff" stroke-width="2"/></svg>CALIBRATION OF PH PROBES</li>
    <li><svg width="24" height="24" viewBox="0 0 24 24"><path d="M20 12a8 8 0 1 1-4-7" fill="none" stroke="#fff" stroke-width="2"/><path d="M8 12l4 4 9-10" fill="none" stroke="#fff" stroke-width="2"/></svg>CONDUCTIVITY PROBE CALIBRATION</li>
    <li><svg width="24" height="24" viewBox="0 0 24 24"><path d="M20 12a8 8 0 1 1-4-7" fill="none" stroke="#fff" stroke-width="2"/><path d="M8 12l4 4 9-10" fill="none" stroke="#fff" stroke-width="2"/></svg>ANALOG LEVEL MANAGEMENT</li>
  </ul>
</section>

<!-- reversible climate control -->
<h2 class="section-title climate-title abs" style="font-size:40px">REVERSIBLE <span>CLIMATE CONTROL</span></h2>
<svg class="abs" style="left:400px;top:2800px" width="420" height="380" viewBox="400 2800 420 380">
  <g fill="none" stroke="#9aa3aa" stroke-width="1.5" stroke-dasharray="4 4">
    <path d="M612 2852a110 110 0 0 1 66 36"/>
    <path d="M690 3042a110 110 0 0 1-50 46"/>
    <path d="M470 2940a110 110 0 0 0 0 70"/>
  </g>
  <circle cx="587" cy="2974" r="104" fill="#fff" stroke="#33a6d7" stroke-width="4"/>
  <circle cx="587" cy="2974" r="92" fill="#e4e4e4"/>
  <text x="587" y="2993" text-anchor="middle" font-family="Poppins, sans-serif" font-weight="700" font-size="52" fill="#2f3a42" letter-spacing="2">ROLV</text>

  <circle cx="456" cy="2859" r="47" fill="#fff" stroke="#33a6d7" stroke-width="3"/>
  <g fill="none" stroke="#2f3a42" stroke-width="2.5" stroke-linecap="round">
    <path d="M438 2841l36 36 M440 2877l14-14 M462 2855l10-10a6 6 0 0 1 6 6"/>
    <path d="M436 2845a6 6 0 0 1 8-8"/>
  </g>
  <circle cx="762" cy="2969" r="47" fill="#fff" stroke="#33a6d7" stroke-width="3"/>
  <g fill="none" stroke="#2f3a42" stroke-width="2.5"><rect x="742" y="2955" width="40" height="28" rx="3"/><path d="M752 2955v-6h20v6 M742 2967h40"/></g>
  <circle cx="494" cy="3121" r="47" fill="#fff" stroke="#33a6d7" stroke-width="3"/>
  <g fill="none" stroke="#2f3a42" stroke-width="2.5"><circle cx="494" cy="3121" r="14"/><circle cx="494" cy="3121" r="5"/><path d="M494 3101v6 M494 3135v6 M474 3121h6 M508 3121h6 M480 3107l4 4 M504 3131l4 4 M508 3107l-4 4 M484 3131l-4 4"/></g>
</svg>
<div class="step right-al abs" style="left:150px;top:2808px;width:225px">
  <h3>INSTALLATION</h3>Lorem Ipsum is simply dummy<br>text of the printing typesetting<br>Lorem Ipsum has been
</div>
<div class="step abs" style="left:835px;top:2918px;width:250px">
  <h3>TROUBLESHOOTING</h3>Lorem Ipsum is simply dummy<br>text of the printing typesetting<br>Lorem Ipsum has been
</div>
<div class="step right-al abs" style="left:185px;top:3090px;width:225px">
  <h3>MAINTENANCE</h3>Lorem Ipsum is simply dummy<br>text of the printing typesetting<br>Lorem Ipsum has been
</div>

<!-- contact -->
<section class="contact abs">
  <h2 class="section-title abs">GET IN TOUCH</h2>
  <div class="field abs" style="left:273px;top:119px;width:314px;height:43px">Your Name</div>
  <div class="field abs" style="left:611px;top:119px;width:316px;height:43px">Email</div>
  <div class="field abs" style="left:273px;top:187px;width:654px;height:101px">Message</div>
  <a class="btn btn-outline send-btn abs" href="#">LEARN MORE</a>
</section>

<!-- footer -->
<footer class="site-footer">
  <div class="brand abs"><span class="brand-mark"></span>ROLV</div>
  <div class="socials abs"><span></span><span></span><span></span><span></span></div>
  <div class="foot-col contact-col abs" style="left:422px;top:3720px;width:260px">
    <h4>CONTACT US</h4>
    <ul>
      <li><svg width="14" height="18" viewBox="0 0 14 18"><path d="M7 1a6 6 0 0 1 6 6c0 4-6 10-6 10S1 11 1 7a6 6 0 0 1 6-6z" fill="none" stroke="#9aa3aa" stroke-width="1.5"/><circle cx="7" cy="7" r="2" fill="#9aa3aa"/></svg><span style="font-size:14px">14 Rue des Tilleuls<br>69003 LYON</span></li>
      <li><svg width="16" height="16" viewBox="0 0 16 16"><path d="M3 1c2-1 3 2 3 3s-2 2-1 3 3 4 4 4 2-2 3-1 3 1 3 3-3 3-6 1-7-6-8-8 0-4 2-5z" fill="#9aa3aa"/></svg><span style="font-size:14px">04 72 10 20 30</span></li>
      <li><svg width="16" height="14" viewBox="0 0 16 14"><rect x="1" y="2" width="14" height="10" fill="none" stroke="#9aa3aa" stroke-width="1.5"/><path d="M1 2l7 6 7-6" fill="none" stroke="#9aa3aa" stroke-width="1.5"/></svg><span style="font-size:14px">contact@rolv-services.fr</span></li>
    </ul>
  </div>
  <div class="foot-col abs" style="left:740px;top:3720px">
    <h4>COMPANY</h4>
    <ul><li>Home</li><li>About Us</li><li>Achievements</li><li>Contact Us</li></ul>
  </div>
  <div class="foot-col abs" style="left:948px;top:3720px">
    <h4>SERVICES</h4>
    <ul><li>Air Conditioning</li><li>Heating</li><li>Air Treatment</li><li>Testimonials</li></ul>
  </div>
  <div class="copyright abs">© 2020 ROLV Services Techniques. All Rights are Reserved.</div>
</footer>

</body>
</html>
```